Keystone Plasterworks Business Card

Looking to update the imagery, colors and logo to a more current design and to reflect their specialty of "High End" residential home construction

```html
<!DOCTYPE html>
<html lang="en">
<head>
<meta charset="utf-8">
<title>Keystone Plasterworks Business Card</title>
<link href="https://fonts.googleapis.com/css2?family=Roboto:wght@400;700;900&display=swap" rel="stylesheet">
<style>
  :root {
    --stage: #2a2a2b;
    --brand-blue: #0a5fb4;
    --brand-blue-light: #1e88d6;
    --brand-navy: #0b3f8f;
    --paper: #f4f5f6;
    --ink: #2b2b2b;
    --white: #ffffff;
  }
  * { box-sizing: border-box; margin: 0; padding: 0; }
  html, body { width: 1200px; height: 1138px; overflow: hidden; background: var(--stage); }
  body { position: relative; font-family: "Roboto", Arial, sans-serif; }

  .card { position: absolute; width: 621px; height: 375px; border-radius: 14px; overflow: hidden; }

  .card-front { left: 274px; top: 186px; background: linear-gradient(180deg, var(--brand-blue) 0%, var(--brand-blue-light) 100%); }
  .front-wordmark {
    position: absolute; top: 52px; left: 0; width: 100%; text-align: center;
    color: var(--white); font-weight: 700; font-size: 44px; letter-spacing: 0.5px;
  }
  .front-photo { position: absolute; top: 142px; height: 156px; }
  .front-photo--left { left: 0; width: 304px; border-radius: 0 16px 16px 0;
    background: linear-gradient(135deg, #e9e6e1 0%, #cfcac2 45%, #8fa7b8 70%, #a89a86 100%); }
  .front-photo--right { left: 318px; width: 303px; border-radius: 16px 0 0 16px;
    background: linear-gradient(135deg, #d8d4cd 0%, #9ea2a6 40%, #4a5058 60%, #b9c6cf 100%); }
  .partner-row { position: absolute; top: 321px; left: 0; width: 100%; display: flex; justify-content: center; gap: 20px; }
  .partner-badge { height: 30px; border-radius: 4px; background: rgba(255,255,255,0.85); }
  .partner-badge--a { width: 120px; }
  .partner-badge--b { width: 134px; }
  .partner-badge--c { width: 128px; }

  .card-back { left: 276px; top: 608px; background: var(--paper); }
  .back-photo { position: absolute; left: 0; top: 0; }
  .back-wordmark {
    position: absolute; right: 24px; top: 58px;
    color: var(--brand-navy); font-weight: 700; font-size: 31px; letter-spacing: 0.3px;
  }
  .contact { position: absolute; right: 24px; text-align: right; color: var(--ink); font-size: 16px; line-height: 1; }
  .contact-name { top: 152px; color: var(--brand-navy); font-weight: 900; font-size: 24px; }
  .contact-role { top: 181px; }
  .contact-line { display: flex; align-items: center; justify-content: flex-end; gap: 8px; }
  .contact-line svg { width: 14px; height: 14px; fill: var(--brand-blue); flex: none; }
  .contact-mobile { top: 207px; }
  .contact-office { top: 276px; }
  .contact-web { top: 300px; color: var(--brand-blue); }
  .contact-email { top: 324px; }
</style>
</head>
<body>

<section class="card card-front">
  <div class="front-wordmark">Keystone Plasterworks</div>
  <div class="front-photo front-photo--left" role="img" aria-label="Bright high-end living room with white sofas, fireplace and coffered ceiling"></div>
  <div class="front-photo front-photo--right" role="img" aria-label="Luxury home entry hall opening onto a two-storey living area"></div>
  <div class="partner-row">
    <div class="partner-badge partner-badge--a"></div>
    <div class="partner-badge partner-badge--b"></div>
    <div class="partner-badge partner-badge--c"></div>
  </div>
</section>

<section class="card card-back">
  <svg class="back-photo" width="290" height="375" viewBox="0 0 290 375">
    <defs>
      <linearGradient id="room-tones" x1="0" y1="0" x2="1" y2="1">
        <stop offset="0" stop-color="#ecebe8"/>
        <stop offset="0.45" stop-color="#d2cbc1"/>
        <stop offset="0.7" stop-color="#9fb6c4"/>
        <stop offset="1" stop-color="#8a7a66"/>
      </linearGradient>
    </defs>
    <path d="M0 0 H214 Q300 180 212 375 H0 Z" fill="var(--brand-blue)"/>
    <path d="M0 0 H206 Q286 180 200 375 H0 Z" fill="url(#room-tones)" role="img" aria-label="Elegant living room with fireplace, chandelier and white armchairs"/>
  </svg>

  <div class="back-wordmark">Keystone Plasterworks</div>

  <div class="contact contact-name">DALE WHITMORE</div>
  <div class="contact contact-role">Founder &amp; Owner</div>
  <div class="contact contact-line contact-mobile">214.555.0148
    <svg viewBox="0 0 24 24"><path d="M6.6 10.8a15 15 0 0 0 6.6 6.6l2.2-2.2c.3-.3.7-.4 1-.2 1.1.4 2.3.6 3.6.6.6 0 1 .4 1 1V20c0 .6-.4 1-1 1A17 17 0 0 1 3 4c0-.6.4-1 1-1h3.5c.6 0 1 .4 1 1 0 1.3.2 2.5.6 3.6.1.3 0 .7-.2 1z"/></svg>
  </div>
  <div class="contact contact-line contact-office">817.555.0273
    <svg viewBox="0 0 24 24"><path d="M3 9c0-2 4-4 9-4s9 2 9 4v2h-5V9H8v2H3zM6 12h12l2 8H4z"/></svg>
  </div>
  <div class="contact contact-line contact-web">KeystonePlasterworks.com
    <svg viewBox="0 0 24 24"><circle cx="12" cy="12" r="10"/><path d="M2 12h20M12 2v20" stroke="#fff" stroke-width="1.5" fill="none"/></svg>
  </div>
  <div class="contact contact-line contact-email">Dale@KeystonePlasterworks.com
    <svg viewBox="0 0 24 24"><path d="M2 5h20v14H2z"/><path d="M2 5l10 8 10-8" stroke="#fff" stroke-width="1.6" fill="none"/></svg>
  </div>
</section>

</body>
</html>
```